Entertainment Sound and Lighting company Business card

We need a professional looking business card designed for my growing entertainment sound and lighting company based in Sydney, Australia called "Kestrel Sound"

We provide technical production services (sound systems/lighting/vision) for events ranging from band gigs, weddings, corporate functions etc.

The business card needs to contain the following information:

Bartholomew Quenneville
Audio Engineer
Phone: 0478 615 702
Email: bartholomew@kestrelsound.com.au
Website: www.kestrelsound.com.au

Business logo has been attached in .ai format, please contact me if you need me to provide other files.

Target Market(s)

We need a business card that reflects our modern and professional company but still looks professional to appeal to our corporate clients.
We have a very broad target market spanning from bands needing PA systems for their gigs (18-30yrs) to event companies needing sound and lighting for weddings and other functions.

Industry/Entity Type

Business

Requirements
Must have
• Needs to include the logo that is attached of course, and the colour scheme.
Nice to have
• - Double sided

```html
<!DOCTYPE html>
<html lang="en">
<head>
<meta charset="utf-8">
<title>Kestrel Sound – Business Card</title>
<link rel="stylesheet" href="https://fonts.googleapis.com/css2?family=Open+Sans:wght@400;700;800&family=Tinos&display=swap">
<style>
  :root {
    --navy: #2b2a6b;
    --cyan: #00b0d8;
    --blue: #1271bb;
    --text-blue: #1a6fb5;
    --white: #ffffff;
  }
  * { margin: 0; padding: 0; box-sizing: border-box; }
  html, body {
    width: 852px; height: 1200px; overflow: hidden;
    background: var(--white);
  }
  .sheet { position: relative; width: 852px; height: 1200px; }

  .card-frame { position: absolute; border: 3px solid var(--navy); }
  .card-inner { position: absolute; border: 3px solid var(--navy); overflow: hidden; }

  /* Front */
  .front-outer { left: 2px; top: 2px; width: 846px; height: 561px; }
  .front-inner { left: 28px; top: 34px; width: 793px; height: 498px; }
  .brand-name {
    position: absolute; left: 0; width: 100%;
    font-family: "Open Sans", sans-serif; font-weight: 800;
    color: var(--blue); text-align: center; letter-spacing: -1px;
  }
  .front-inner .brand-name { top: 200px; font-size: 64px; }
  .name-band {
    position: absolute; left: 0; right: 0; bottom: 0; height: 152px;
    background: var(--cyan); color: var(--white);
    font-family: "Tinos", serif; text-align: center;
  }
  .person-name { margin-top: 38px; font-size: 29px; letter-spacing: 0.5px; transform: scaleX(0.88); }
  .person-role { margin-top: 6px; font-size: 32px; transform: scaleX(0.9); }

  /* Back */
  .back-outer { left: 5px; top: 637px; width: 845px; height: 561px; }
  .back-inner { left: 32px; top: 667px; width: 792px; height: 500px; }
  .back-inner .brand-name {
    top: 130px; left: 28px; width: auto; text-align: left; font-size: 44px;
  }
  .contact {
    position: absolute; font-family: "Open Sans", sans-serif;
    color: var(--text-blue);
  }
  .contact-phone { top: 46px; right: 30px; font-size: 26px; }
  .contact-online { top: 386px; left: 258px; font-size: 24px; line-height: 38px; }
  .services-band {
    position: absolute; left: 0; right: 0; top: 240px; height: 89px;
    background: var(--blue); color: var(--white);
    font-family: "Open Sans", sans-serif; font-size: 19.5px; line-height: 28px;
    text-align: center; padding-top: 16px;
  }
</style>
</head>
<body>
<div class="sheet">
  <section class="card-frame front-outer"></section>
  <section class="card-inner front-inner">
    <div class="brand-name">Kestrel Sound</div>
    <div class="name-band">
      <p class="person-name">BARTHOLOMEW QUENNEVILLE</p>
      <p class="person-role">Audio Engineer</p>
    </div>
  </section>

  <section class="card-frame back-outer"></section>
  <section class="card-inner back-inner">
    <div class="brand-name">Kestrel Sound</div>
    <p class="contact contact-phone">Phone: 0478 615 702</p>
    <div class="services-band">
      <p>We provide technical production services (sound systems/lighting/vision)</p>
      <p>for events ranging from band gigs, weddings, corporate functions etc.</p>
    </div>
    <div class="contact contact-online">
      <p>Email: bartholomew@kestrelsound.com.au</p>
      <p>Website: www.kestrelsound.com.au</p>
    </div>
  </section>
</div>
</body>
</html>
```